3月15日にガールズバーをオープン致しました。
ビルの入り口に置いて使うA1立て看板の製作をお願いします。
A4など縮小サイズでもいただけると助かります。
白を基調とした夜でも目立つ感じにしたいです。

セット料金 40分2000円 tax&service 20%

チャージのみ1時間1500円 tax&service 15

クレジットチャージ 10%
飲み放題付き (焼酎 ウイスキー カクテルなど)
ビル3階 席数17席  団体客歓迎

若いギャル系の女の子の写真を大きく入れて頂きたいのですが素材が無く
困ってます。素材をお持ちかたにお願いしたいと思ってます。

現在の看板を添付致しました。ご参考までに。
文章は記載しないでも大丈夫です。

店舗名 Sunflower(サンフラワー)です。

よろしくお願いします。
資料を再添付致しました。よろしくお願いします。
依頼金額を25000円に変更して、延長しました。
提案下さった皆様ありがとうございます。
もう少し提案を見させていただけたらと思います。

具体的なイメージをデザベース様の過去の事例で近いものを添付致しました。
よろしくお願いします。

最初に思い描いてたイメージより良かったです
女の子と背景のピンクもかわいいくて満足です。

ありがとうございました!

提案くださった皆様ありがとうございます!
修正をしてくださった皆様も早急な対応に感謝致します。

ありがとうございました!

```html
<!DOCTYPE html>
<html lang="ja">
<head>
<meta charset="utf-8">
<title>Girls Bar Sunflower</title>
<link href="https://fonts.googleapis.com/css2?family=Oswald:wght@600&family=Yellowtail&family=Noto+Serif+JP:wght@700;900&family=M+PLUS+Rounded+1c:wght@700;800&display=swap" rel="stylesheet">
<style>
  :root {
    --pink: #e8447a;
    --pink-deep: #d8255f;
    --pink-soft: #f7b7cc;
    --pink-pale: #fde6ee;
    --red: #e2213f;
    --ribbon: #c8102e;
    --ribbon-dark: #8e0a20;
    --white: #ffffff;
    --ink: #d6336c;
  }
  * { margin: 0; padding: 0; box-sizing: border-box; }
  html, body { width: 859px; height: 1200px; overflow: hidden; background: var(--white); }
  .poster {
    position: relative; width: 859px; height: 1200px; overflow: hidden;
    background: linear-gradient(to bottom, var(--white) 0%, var(--white) 84%, var(--pink-pale) 90%, var(--pink-soft) 100%);
    font-family: "Noto Serif JP", serif;
  }
  .top-band {
    position: absolute; left: 0; top: 0; width: 100%; height: 98px;
    background: linear-gradient(to bottom, #f06a97, var(--pink-deep));
    display: flex; align-items: center; justify-content: center;
  }
  .top-band span {
    font-family: "Oswald", sans-serif; font-weight: 600; color: var(--white);
    font-size: 58px; letter-spacing: 3px;
  }
  .kana-name {
    position: absolute; top: 112px; left: 0; width: 100%; text-align: center;
    font-family: "M PLUS Rounded 1c", sans-serif; font-weight: 800;
    color: var(--red); font-size: 27px; letter-spacing: 2px;
  }
  .shop-name {
    position: absolute; top: 128px; left: 0; width: 100%; text-align: center;
    font-family: "Yellowtail", cursive; color: var(--pink-deep);
    font-size: 170px; line-height: 1;
  }
  .photo {
    position: absolute; left: 0; top: 300px; width: 859px; height: 520px;
    background: radial-gradient(ellipse at 45% 45%, #e9cdbf 0%, #d9b09c 35%, #f4e6df 70%, var(--white) 100%);
  }
  .catch {
    position: absolute; right: 40px; top: 300px; text-align: center;
    font-family: "M PLUS Rounded 1c", sans-serif; font-weight: 700;
    color: var(--pink); font-size: 30px; line-height: 1.35;
  }
  .ribbon { position: absolute; left: 140px; top: 790px; width: 580px; height: 120px; }
  .prices { position: absolute; left: 0; top: 0; width: 100%; color: var(--ink); }
  .price-row {
    position: absolute; left: 0; width: 100%; height: 44px;
    font-weight: 900; font-size: 30px; white-space: nowrap;
  }
  .price-row .label { position: absolute; left: 120px; bottom: 0; }
  .price-row .yen { position: absolute; left: 545px; bottom: 0; }
  .price-row .tax { position: absolute; left: 690px; bottom: 6px; font-size: 14px; font-weight: 700; }
  .price-row.set { top: 905px; }
  .price-row.charge { top: 955px; }
  .credit {
    position: absolute; top: 1012px; left: 0; width: 100%; text-align: center;
    font-weight: 700; font-size: 24px; color: var(--ink); white-space: nowrap;
  }
  .group-badge {
    position: absolute; left: 22px; top: 1050px; width: 145px; height: 145px; border-radius: 50%;
    background: var(--pink-deep); color: var(--white);
    display: flex; align-items: center; justify-content: center; text-align: center;
    font-family: "M PLUS Rounded 1c", sans-serif; font-weight: 800; font-size: 38px; line-height: 1.15;
  }
  .floor-info {
    position: absolute; left: 195px; width: 360px; top: 1070px; text-align: center;
    font-family: "M PLUS Rounded 1c", sans-serif; font-weight: 800; color: var(--red);
    line-height: 1.1;
  }
  .floor-info .floor { font-size: 46px; display: block; }
  .floor-info .seats { font-size: 34px; display: block; }
  .drinks-box {
    position: absolute; right: 18px; top: 1058px; width: 250px; height: 128px;
    background: var(--pink-deep); color: var(--white); text-align: center;
    font-family: "M PLUS Rounded 1c", sans-serif; font-weight: 800;
    display: flex; flex-direction: column; justify-content: center;
  }
  .drinks-box .head { font-size: 40px; line-height: 1.2; }
  .drinks-box .list { font-size: 21px; line-height: 1.3; }
</style>
</head>
<body>
<div class="poster">
  <header class="top-band"><span>GIRLS BAR</span></header>
  <div class="kana-name">ガールズバー・サンフラワー</div>
  <div class="shop-name">Sunflower</div>

  <div class="photo" role="img" aria-label="笑顔の若い女性二人が背中合わせに並ぶ写真"></div>
  <div class="catch">可愛い子たちと<br>気軽に遊べる！</div>

  <svg class="ribbon" viewBox="0 0 580 120" aria-label="NEW OPEN">
    <polygon points="0,30 80,30 80,100 0,100 28,65" fill="var(--ribbon-dark)"/>
    <polygon points="580,30 500,30 500,100 580,100 552,65" fill="var(--ribbon-dark)"/>
    <path d="M60,20 Q290,60 520,20 L520,90 Q290,130 60,90 Z" fill="var(--ribbon)"/>
    <text x="290" y="80" text-anchor="middle" font-family="Oswald, sans-serif" font-weight="600" font-size="40" fill="#fff" font-style="italic" letter-spacing="2">NEW OPEN</text>
  </svg>

  <section class="prices">
    <div class="price-row set"><span class="label">セット料金 40分・・・・・・</span><span class="yen">￥2,000</span><span class="tax">tax &amp; service 20%</span></div>
    <div class="price-row charge"><span class="label">チャージのみ 1時間・・・・・</span><span class="yen">￥1,500</span><span class="tax">tax &amp; service 15%</span></div>
    <div class="credit">クレジットチャージ　10%</div>
  </section>

  <div class="group-badge">団体客<br>歓迎</div>
  <div class="floor-info"><span class="floor">当ビル3階</span><span class="seats">座席17席</span></div>
  <div class="drinks-box">
    <div class="head">飲み放題付</div>
    <div class="list">焼酎・ウイスキー<br>カクテルなど</div>
  </div>
</div>
</body>
</html>
```